Animal Facility Brochure for Pet Boarding, Boutique, Doggie Daycare, Grooming

This brochure is for a Doggie Daycare, Pet Grooming, Dog Boarding & Pet Boutique for the Hollowmere Pet Lodge & Spa.

Hi there! I am in need of a brochure done for my new up and coming business.
The business will involve Dog/Cat Grooming, Dog Boarding, Doggie Daycare, & a small pet boutique. I am looking for something that stands out and is modern and chic and follows the look of the pictures i have posted (Pim and Tessel) . My color scheme of my business is gray & white. Also i need the brochure to be easily able to understand what we are trying to get across and is easy to read. I am very proud of my logo that was created using craft hive and would love that incorporated. also i have attached the information that will need to be in the brochure for the client. I am looking for someone who can devote some time working with me on this because this is my first time. I am sure there will need to be some changes so i need someone who is patient. The picture of the projected look of my sign is gearing more towards something clean and modern.

Industry/Entity Type

Pet Care

Colors
f5f5f5
f8f8f8
dbdbdb
959595
aaaaaa
85abd2
cedeed
eaf1f7

Requirements
Nice to have
• File nine for Grooming, Boarding, Daycare, Pet Boutique

```html
<!DOCTYPE html>
<html lang="en">
<head>
<meta charset="utf-8">
<title>Hollowmere Pet Lodge &amp; Spa – Brochure</title>
<link rel="stylesheet" href="https://fonts.googleapis.com/css2?family=Cinzel:wght@400;600&family=Crimson+Text:ital,wght@0,400;0,600;1,400&display=swap">
<style>
  :root{
    --stage:#ececec;
    --paper:#f8f8f8;
    --slate-blue:#6f8aab;
    --slate-blue-dark:#5f7a9b;
    --warm-gray:#7b7570;
    --warm-gray-dark:#6d6762;
    --ink:#4a4845;
    --white:#ffffff;
    --tick:#85abd2;
    --rule:#dbdbdb;
  }
  *{box-sizing:border-box;margin:0;padding:0}
  html,body{width:1200px;height:840px;overflow:hidden;background:var(--stage)}
  body{font-family:"Crimson Text",Georgia,serif;color:var(--white)}
  .canvas{position:relative;width:1200px;height:840px;padding:20px 30px;display:flex;flex-direction:column;gap:20px}
  .sheet{display:flex;width:1140px;height:390px;background:var(--paper);box-shadow:0 2px 8px rgba(0,0,0,.15)}
  .panel{position:relative;width:380px;height:390px;display:flex;flex-direction:column;overflow:hidden}
  .panel + .panel{border-left:1px solid rgba(0,0,0,.08)}
  .block{padding:12px 20px}
  .block--blue{background:var(--slate-blue)}
  .block--gray{background:var(--warm-gray)}
  .block--white{background:var(--paper);color:var(--ink)}
  .heading{font-family:"Cinzel",Georgia,serif;font-weight:400;font-size:17px;letter-spacing:.06em;text-transform:uppercase;margin-bottom:6px}
  .body-copy{font-size:10.5px;line-height:1.32;text-align:justify}
  .photo{flex:none;width:100%}
  /* outside panels */
  .photo--pups{height:120px;background:linear-gradient(90deg,#f3f1ee 0%,#e4ded6 35%,#cdc4b8 60%,#f1efec 100%)}
  .mission{height:175px}
  .statement{flex:1;display:flex;align-items:center;justify-content:center;text-align:center;font-family:"Cinzel",Georgia,serif;font-size:14px;line-height:1.45;letter-spacing:.05em;padding:10px 24px}
  .hours{height:185px;text-align:center}
  .hours .heading{margin-bottom:10px}
  .hours-list{list-style:none;font-size:11px;line-height:1.55}
  .photo--shop{flex:1;background:linear-gradient(180deg,#e8e2d9 0%,#b89d80 45%,#7a5c44 80%,#5b4535 100%)}
  .cover{flex:1;position:relative;background:linear-gradient(110deg,#8f8a86 0%,#b2aaa2 35%,#d7cfc4 60%,#a69483 100%)}
  .cover-title{position:absolute;top:24px;left:24px;font-family:"Cinzel",Georgia,serif;font-size:22px;line-height:1.2;letter-spacing:.05em;text-transform:uppercase;color:var(--white)}
  /* inside panels */
  .about{height:165px}
  .photo--rack{height:90px;background:linear-gradient(90deg,#c9b9a4 0%,#8d8a7e 30%,#efece7 55%,#d8d3cc 100%)}
  .grooming{flex:1}
  .daycare{height:120px}
  .photo--interior{height:120px;background:linear-gradient(90deg,#efece7 0%,#cfc7bc 35%,#9c8c7a 60%,#e6e1da 100%)}
  .pricing{flex:1}
  .pricing .body-copy{font-size:9.6px;line-height:1.3}
  .pricing ul{list-style:none}
  .stay{height:255px}
  .stay .heading{color:var(--warm-gray-dark);font-size:16px}
  .stay-list{list-style:none;font-size:9.8px;line-height:1.28;color:var(--ink)}
  .stay-list li{display:flex;gap:7px;padding:3px 0;border-bottom:1px solid var(--rule)}
  .stay-list svg{flex:none;width:11px;height:11px;margin-top:2px}
  .photo--bags{flex:1;background:linear-gradient(90deg,#a89279 0%,#d6c8b3 40%,#e9e0d2 65%,#cfc5b8 100%)}
</style>
</head>
<body>
<main class="canvas">

  <!-- outside of the trifold -->
  <section class="sheet sheet--outside">
    <article class="panel">
      <div class="photo photo--pups" role="img" aria-label="Photo of two French bulldogs beside a cushioned dog bed"></div>
      <div class="block block--blue mission">
        <h2 class="heading">Our Mission:</h2>
        <p class="body-copy">It is our goal to give your pet a safe, happy and caring place to stay while you are away. We treat every guest like family, offering clean suites, gentle hands and plenty of play. Our trained team keeps each pet comfortable, active and loved, so you can travel with total peace of mind knowing they are well cared for every day.</p>
      </div>
      <div class="block--gray statement">We provide a social experience for dogs &amp; cats &amp; a new standard for dog care</div>
    </article>

    <article class="panel">
      <div class="block block--blue hours">
        <h2 class="heading">Hours of Operation</h2>
        <ul class="hours-list">
          <li>Monday 7:00am – 6:30pm</li>
          <li>Tuesday 7:00am – 6:30pm</li>
          <li>Wednesday 7:00am – 6:30pm</li>
          <li>Thursday 7:00am – 6:30pm</li>
          <li>Friday 7:00am – 6:30pm</li>
          <li>Saturday 8:00am – 4:00pm</li>
          <li>Sunday 10:00am – 4:00pm</li>
        </ul>
      </div>
      <div class="photo photo--shop" role="img" aria-label="Photo of the boutique interior with wooden shelves of pet goods"></div>
    </article>

    <article class="panel">
      <div class="cover" role="img" aria-label="Photo of a woman in a knit wrap holding a pug on a leash inside the boutique"></div>
      <h1 class="cover-title">Healthy,<br>Happy and<br>Well-Loved</h1>
    </article>
  </section>

  <!-- inside of the trifold -->
  <section class="sheet sheet--inside">
    <article class="panel">
      <div class="block block--blue about">
        <h2 class="heading">About Us:</h2>
        <p class="body-copy">Hollowmere Pet Lodge &amp; Spa is a high-quality, full-service pet facility with grooming, daycare, boarding and a boutique. We give every pet the trust, care and attention they deserve. Our caring team brings years of experience, and our modern spaces are designed for comfort, safety and fun. We make time to get to know each guest and meet their unique needs.</p>
      </div>
      <div class="photo photo--rack" role="img" aria-label="Photo of a rack of pet coats beside a white treat canister"></div>
      <div class="block block--blue grooming">
        <h2 class="heading">Grooming</h2>
        <p class="body-copy">At Hollowmere Pet Lodge &amp; Spa our experienced grooming staff will take the time to make your pet look and feel its very best. Every groom includes a warm bath, brushing, nail trim and ear cleaning. Our groomers use gentle, quality products and work at a calm pace. Packages range from a simple wash to a full breed-standard style, and each service is tailored to your pet's coat, size and temperament.</p>
      </div>
    </article>

    <article class="panel">
      <div class="block block--gray daycare">
        <h2 class="heading">Daycare</h2>
        <p class="body-copy">Our daycare play rooms are supervised by our trained staff, who make sure every dog is safe and happy. Dogs are grouped by size and play style, and enjoy games, rest time and lots of attention. It is a social day your dog will love.</p>
      </div>
      <div class="photo photo--interior" role="img" aria-label="Photo of the lodge lounge with shelves, a bench and a dog bed"></div>
      <div class="block block--gray pricing">
        <h2 class="heading">Pricing</h2>
        <div class="body-copy">
          <p>We require all guests to complete an evaluation prior to entering our daycare program. This evaluation will determine whether your pet is safe to play with other dogs and members of our staff.</p>
          <p>For all canine guests:</p>
          <ul>
            <li>• Proof of current DHPP/DHPP2 (yearly), Rabies, and Bordetella (yearly).</li>
            <li>• All vaccinations must be current before lodging/daycare.</li>
          </ul>
          <p>For all feline guests:</p>
          <ul>
            <li>• Proof of current Rabies and FVRCP.</li>
            <li>• All vaccinations must be current before lodging.</li>
          </ul>
        </div>
      </div>
    </article>

    <article class="panel">
      <div class="block block--white stay">
        <h2 class="heading">While Your Dog Is With Us</h2>
        <ul class="stay-list">
          <li><svg viewBox="0 0 12 12" aria-hidden="true"><path d="M1.5 6.5l3 3 6-7" fill="none" stroke="var(--tick)" stroke-width="2"/></svg>Supervised off leash dog daycare</li>
          <li><svg viewBox="0 0 12 12" aria-hidden="true"><path d="M1.5 6.5l3 3 6-7" fill="none" stroke="var(--tick)" stroke-width="2"/></svg>We offer 24/7 supervision to ensure a safe, relaxing and stress-free environment</li>
          <li><svg viewBox="0 0 12 12" aria-hidden="true"><path d="M1.5 6.5l3 3 6-7" fill="none" stroke="var(--tick)" stroke-width="2"/></svg>Pet boutique with toys, treats, beds, clothes, leashes and more</li>
          <li><svg viewBox="0 0 12 12" aria-hidden="true"><path d="M1.5 6.5l3 3 6-7" fill="none" stroke="var(--tick)" stroke-width="2"/></svg>Climate controlled rooms and trained staff to provide the best care</li>
          <li><svg viewBox="0 0 12 12" aria-hidden="true"><path d="M1.5 6.5l3 3 6-7" fill="none" stroke="var(--tick)" stroke-width="2"/></svg>Elevated beds &amp; soft, fleece-lined bedding throughout the stay</li>
          <li><svg viewBox="0 0 12 12" aria-hidden="true"><path d="M1.5 6.5l3 3 6-7" fill="none" stroke="var(--tick)" stroke-width="2"/></svg>Outdoor walks provided and play sessions throughout the day</li>
          <li><svg viewBox="0 0 12 12" aria-hidden="true"><path d="M1.5 6.5l3 3 6-7" fill="none" stroke="var(--tick)" stroke-width="2"/></svg>Opportunity to play in our daycare with other dogs under trained staff supervision</li>
        </ul>
      </div>
      <div class="photo photo--bags" role="img" aria-label="Photo of burlap treat bags and a bowl on a wooden shelf"></div>
    </article>
  </section>

</main>
</body>
</html>
```